Cybersecurity company is looking for business card.

I need a business card design for our company, we are a cybersecurity company providing advance technology to protect agains any kind of malware. We need a fresh modern design it should communicate modern, technology and growth.

Target Market(s)

Business to business

Industry/Entity Type

Business

Contact Information for Business Card

Should have location, address, fax, mobile, phone, email and website.

Requirements
Must have
• Must follow company's logo color and style. Must have the company's log on its.

```html
<!DOCTYPE html>
<html lang="en">
<head>
<meta charset="utf-8">
<title>Vartelo – Business Card</title>
<link rel="stylesheet" href="https://fonts.googleapis.com/css2?family=Open+Sans:wght@600;700;800&display=swap">
<style>
  :root {
    --ink: #000000;
    --brand-red: #a10d0f;
    --paper: #ffffff;
    --backdrop: #e9e6e2;
  }
  * { margin: 0; padding: 0; box-sizing: border-box; }
  html, body {
    width: 1200px; height: 954px; overflow: hidden;
    background: var(--backdrop);
    font-family: "Open Sans", Arial, sans-serif;
  }
  .canvas { position: relative; width: 1200px; height: 954px; }

  .card {
    position: absolute;
    width: 560px; height: 320px;
    border-radius: 4px;
    overflow: hidden;
    box-shadow: 0 10px 28px rgba(0,0,0,.22);
  }
  .card-back  { left: 70px;  top: 110px; }
  .card-front { left: 570px; top: 520px; }

  .card-shapes { position: absolute; inset: 0; width: 100%; height: 100%; }

  .wordmark {
    position: absolute;
    display: flex; align-items: center; gap: 8px;
    color: var(--paper);
    font-weight: 800;
    font-size: 46px;
    letter-spacing: 1px;
    line-height: 1;
  }
  .wordmark-dot { width: 9px; height: 9px; background: var(--brand-red); }
  .card-back .wordmark  { left: 52px;  top: 136px; }
  .card-front .wordmark { left: 168px; top: 120px; }

  .contact-list {
    position: absolute; left: 360px; top: 34px;
    list-style: none;
    color: var(--paper);
    font-weight: 700;
    font-size: 14px;
  }
  .contact-item { display: flex; align-items: center; gap: 8px; height: 25px; }
  .contact-icon { width: 16px; height: 16px; fill: none; stroke: var(--paper); stroke-width: 1.6; }
  .contact-icon.solid { fill: var(--paper); stroke: none; }
  .contact-item.indent { padding-left: 24px; }

  .address {
    position: absolute; left: 396px; top: 216px;
    color: var(--paper);
    font-weight: 700;
    font-size: 14px;
    line-height: 24px;
  }
  .address-line { display: flex; align-items: center; gap: 8px; }
  .address-line.indent { padding-left: 24px; }
</style>
</head>
<body>
<main class="canvas">

  <!-- Contact side -->
  <section class="card card-back" aria-label="Business card, contact side">
    <svg class="card-shapes" viewBox="0 0 560 320" aria-hidden="true">
      <rect width="560" height="320" fill="var(--brand-red)"/>
      <path d="M0 0 H310 V56 H322 Q340 56 340 74 V236 Q340 252 322 252 H300 L300 320 H0 Z" fill="var(--ink)"/>
      <path d="M0 118 H16 Q30 118 30 134 V270 Q30 286 16 286 H0 Z" fill="var(--brand-red)"/>
      <path d="M300 320 V308 Q300 296 314 296 H410 Q424 296 424 308 V320 Z" fill="var(--brand-red)"/>
    </svg>

    <div class="wordmark"><span class="wordmark-dot"></span>vartelo</div>

    <ul class="contact-list">
      <li class="contact-item">
        <svg class="contact-icon" viewBox="0 0 16 16"><rect x="4" y="1" width="8" height="14" rx="1.5"/><line x1="7" y1="12.5" x2="9" y2="12.5"/></svg>
        555-318-42
      </li>
      <li class="contact-item">
        <svg class="contact-icon solid" viewBox="0 0 16 16"><path d="M3 1.5 L6 1 L7.5 4.5 L5.6 6 Q7 9 10 10.4 L11.5 8.5 L15 10 L14.5 13 Q13.8 15 11.5 14.6 Q4 12.5 1.4 4.5 Q1 2.2 3 1.5 Z"/></svg>
        555-907-63
      </li>
      <li class="contact-item">fax: 555-460-19</li>
      <li class="contact-item">
        <svg class="contact-icon" viewBox="0 0 16 16"><rect x="1" y="3" width="14" height="10"/><polyline points="1,3 8,9 15,3"/></svg>
        nadia@vartelo.com
      </li>
      <li class="contact-item indent">www.vartelosec.io</li>
    </ul>

    <address class="address" style="font-style:normal">
      <div class="address-line">
        <svg class="contact-icon solid" viewBox="0 0 16 16"><path d="M8 1 L15.5 8 H13 V15 H9.5 V10.5 H6.5 V15 H3 V8 H0.5 Z"/></svg>
        118 Orchard lane
      </div>
      <div class="address-line indent">40215 Lyon, France</div>
    </address>
  </section>

  <!-- Logo side -->
  <section class="card card-front" aria-label="Business card, logo side">
    <svg class="card-shapes" viewBox="0 0 560 320" aria-hidden="true">
      <rect width="560" height="320" fill="var(--ink)"/>
      <path d="M0 226 H292 V240 Q292 262 314 262 H438 Q458 262 458 240 V214 Q458 200 476 200 H560 V320 H0 Z" fill="var(--brand-red)"/>
    </svg>
    <div class="wordmark"><span class="wordmark-dot"></span>vartelo</div>
  </section>

</main>
</body>
</html>
```